Packaging design coffee brand

Creating a packaging design for coffee products. an existing brand shall be repositioned, complete redesign. capsules, beans, etc. We need a label for the coffee whole bean package, a folded packaging for coffee capsules, see attachment. The package for the whole bean also shall be changed into a full printed packaging.

The logo is already created, but you can play with the elements, the position of symbol and name.

Target Market(s)

Europe

Industry/Entity Type

coffee

Font styles to use
Sans Serif

Requirements
Must have
• we already have a logo, which shall be used. Position of the symbol and name can be adjusted.
Nice to have
• please see the briefing attached, there you find al relevant information.
Should not have
• shall not be ecological, it shal be a lifestyle brand.

```html
<!DOCTYPE html>
<html lang="en">
<head>
<meta charset="UTF-8">
<title>Vero Calma – Whole Bean Coffee Pack</title>
<link href="https://fonts.googleapis.com/css2?family=Barlow:wght@400;500&family=Courier+Prime:wght@400;700&display=swap" rel="stylesheet">
<style>
  :root {
    --page-bg: #f4f4f4;
    --pack-orange: #f3a62a;
    --pack-orange-deep: #e88e14;
    --brand-green: #438a0c;
    --brand-green-deep: #2f6f08;
    --ink: #1a1208;
    --white: #ffffff;
  }
  * { margin: 0; padding: 0; box-sizing: border-box; }
  html, body {
    width: 1200px;
    height: 960px;
    overflow: hidden;
    background: var(--page-bg);
  }
  .canvas {
    position: relative;
    width: 1200px;
    height: 960px;
  }
  .pack-front {
    position: absolute;
    left: 420px;
    top: 70px;
    width: 360px;
    height: 820px;
    background: linear-gradient(180deg, var(--pack-orange) 0%, var(--pack-orange) 60%, var(--pack-orange-deep) 100%);
    overflow: hidden;
  }
  .brand-disc {
    position: absolute;
    left: 50px;
    top: 190px;
    width: 420px;
    height: 420px;
    border-radius: 50%;
    background: linear-gradient(200deg, var(--brand-green) 0%, var(--brand-green) 55%, var(--brand-green-deep) 100%);
  }
  .brand-name {
    position: absolute;
    left: 150px;
    top: 512px;
    width: 150px;
    text-align: center;
    font-family: "Barlow", sans-serif;
    font-weight: 500;
    font-size: 21px;
    letter-spacing: 1.5px;
    color: var(--white);
  }
  .product-label {
    position: absolute;
    left: 36px;
    right: 24px;
    top: 628px;
    color: var(--ink);
  }
  .roast {
    font-family: "Barlow", sans-serif;
    font-size: 12px;
    letter-spacing: 4px;
    text-align: right;
    padding-right: 60px;
  }
  .coffee-type {
    font-family: "Courier Prime", monospace;
    font-weight: 700;
    font-size: 45px;
    line-height: 1;
    letter-spacing: -1px;
    text-align: center;
    padding: 2px 0 4px;
    border-bottom: 1.5px solid var(--ink);
    white-space: nowrap;
  }
  .spec-row {
    display: flex;
    border-bottom: 1.5px solid var(--ink);
  }
  .spec {
    flex: 1;
    font-family: "Courier Prime", monospace;
    text-align: center;
  }
  .spec + .spec { border-left: 1.5px solid var(--ink); }
  .spec-grind {
    font-weight: 700;
    font-size: 22px;
    letter-spacing: 6px;
    padding: 22px 0 4px;
  }
  .spec-weight {
    font-size: 28px;
    letter-spacing: 3px;
    line-height: 1;
    padding-top: 6px;
  }
  .spec-weight small {
    display: block;
    font-size: 10px;
    font-weight: 700;
    letter-spacing: 1px;
    padding-top: 2px;
  }
  .claim {
    font-family: "Courier Prime", monospace;
    font-weight: 700;
    font-size: 8px;
    letter-spacing: 1px;
    text-align: center;
    line-height: 1.3;
    padding-top: 6px;
  }
</style>
</head>
<body>
<main class="canvas">
  <section class="pack-front">
    <div class="brand-disc"></div>
    <span class="brand-name">VERO CALMA</span>
    <div class="product-label">
      <p class="roast">MEDIUM ROAST</p>
      <h1 class="coffee-type">COFFEE TYPE</h1>
      <div class="spec-row">
        <p class="spec spec-grind">WHOLE</p>
        <p class="spec spec-weight">12OZ<small>340g</small></p>
      </div>
      <p class="claim">HIGH QUALITY COFFEE WHICH STANDS FOR<br>SUSTAINABILTY, CLIMA AND FAIR TRADE</p>
    </div>
  </section>
</main>
</body>
</html>
```